Business Card Design for Orthopaedic Surgeon

This is a double-sided glossy business card. I prefer baby blue, teal, and green as color schemes. I have my logo already (many colors that you can choose from). I have photos and examples of my old card (very bland but has the information in it). I also have one that my assistant tried to design, but the writing is too small and I don't love the formatting. But it is close!
I would like my logo to be on the business card but I'm uploading my logo in many different colors so you can choose which one looks best based on the color scheme. I also uploaded many sized headshots so you can choose the best resolution one.

Additional information:
Correct business address:
4382 NW 58th Lane, Suite 305
Tamarac, FL 33417

Everything else on both business cards are accurate.

I actually need 2 different business cards generated. One that includes my cell phone number-- Personal cell: 585-314-9062 in addition to Office phone: (954) 316-4870 and Office Fax: 954-316-4881. Again, one card would have my personal cell and one wouldn't

Overall I just think the baby blue card (uploaded) is missing something on the front--of course it is also missing my office phone/fax/personal cell. I do want my website on the front too. Email: info@wellsorthocare.example

You can use your discretion about what goes on the front vs. what goes on the back to eliminated clutter.

Oh and on the back, I would like to list "Conditions Treated" (not specialties include). The list is:
Carpal Tunnel
Trigger Finger
Ganglion Cysts
Hand Tumors
Han & Wrist Arthritis
Hand, Wrist & Elbow Tendonitis
Fractures of the Hand, Wrist, Elbow and Humerus
Nerve Injuries of the Hand, Wrist & Elbow
Microsurgery
Wrist Arthroscopy
Endoscopic Surgery

Target Market(s)

Primary care doctors, Lawyers, patients

Industry/Entity Type

Medical

Contact Information for Business Card

Please see above in project description

Colors

Designer to choose colors to be used in the design.

Requirements
Must have
• -Correct office info, Board Certified Orthopaedic Hand & Upper Extremity Surgeon
Nice to have
• Something that is classy and wow!

```html
<!DOCTYPE html>
<html lang="en">
<head>
<meta charset="utf-8">
<title>Dana Wells, M.D. – Business Card</title>
<link href="https://fonts.googleapis.com/css2?family=Montserrat:wght@400;500;600;700&display=swap" rel="stylesheet">
<style>
  :root {
    --baby-blue: #7cc1ea;
    --accent-blue: #5ab4e6;
    --teal: #1fa8b5;
    --ink: #3d3d3d;
    --white: #ffffff;
    --stage: #eef1f4;
    --photo-top: #3a2a24;
    --photo-bottom: #1c1c1f;
  }
  * { box-sizing: border-box; margin: 0; padding: 0; }
  html, body { width: 1200px; height: 913px; overflow: hidden; }
  body {
    background: var(--stage);
    font-family: "Montserrat", sans-serif;
    display: flex;
    flex-direction: column;
    align-items: center;
    justify-content: center;
    gap: 40px;
  }
  .card {
    width: 700px;
    height: 400px;
    border-radius: 22px;
    position: relative;
    overflow: hidden;
    box-shadow: 0 10px 28px rgba(0,0,0,0.18);
  }

  /* Back side */
  .card-back {
    background: var(--baby-blue);
    color: var(--white);
    text-align: center;
    padding-top: 40px;
  }
  .brand {
    display: flex;
    align-items: center;
    justify-content: center;
    gap: 14px;
  }
  .brand-dot {
    width: 54px; height: 54px;
    border-radius: 50%;
    border: 3px solid var(--white);
  }
  .brand-name {
    font-weight: 600;
    font-size: 30px;
    letter-spacing: 4px;
  }
  .conditions-heading {
    display: flex;
    align-items: center;
    gap: 14px;
    margin: 34px 46px 14px;
    font-weight: 700;
    font-size: 22px;
    letter-spacing: 0.5px;
    white-space: nowrap;
  }
  .conditions-heading::before,
  .conditions-heading::after {
    content: "";
    flex: 1;
    height: 2px;
    background: var(--white);
  }
  .conditions-list {
    font-weight: 500;
    font-size: 17.5px;
    line-height: 1.5;
    padding: 0 30px;
  }

  /* Front side */
  .card-front {
    background: var(--white);
    color: var(--ink);
  }
  .edge-tab {
    position: absolute;
    left: -8px; top: 118px;
    width: 22px; height: 36px;
    border-radius: 8px;
    background: var(--baby-blue);
  }
  .details {
    position: absolute;
    left: 46px; top: 44px;
    width: 400px;
  }
  .doctor-name {
    color: var(--accent-blue);
    font-weight: 600;
    font-size: 26px;
    letter-spacing: 1.5px;
  }
  .credentials {
    font-size: 18px;
    line-height: 1.35;
    margin-top: 6px;
  }
  .address {
    font-size: 18px;
    line-height: 1.35;
    margin-top: 26px;
  }
  .contact-list {
    list-style: none;
    margin-top: 26px;
    font-size: 17px;
    line-height: 1.45;
  }
  .contact-list li {
    display: flex;
    align-items: center;
    gap: 10px;
  }
  .contact-list svg { width: 16px; height: 16px; flex: none; }
  .headshot {
    position: absolute;
    right: 0; top: 0;
    width: 260px; height: 300px;
    background: linear-gradient(180deg, var(--photo-top), var(--photo-bottom));
    border-bottom-left-radius: 40px;
  }
  .hand-art {
    position: absolute;
    right: 200px; bottom: 50px;
    width: 190px; height: 70px;
    border-radius: 35px;
    background: linear-gradient(90deg, rgba(124,193,234,0.35), rgba(124,193,234,0.15));
  }
</style>
</head>
<body>

<section class="card card-back">
  <div class="brand">
    <span class="brand-dot"></span>
    <span class="brand-name">WELLS HAND</span>
  </div>
  <h2 class="conditions-heading">CONDITIONS TREATED</h2>
  <p class="conditions-list">
    Carpal Tunnel • Trigger Finger • Ganglion Cysts • Hand Tumors<br>
    Han &amp; Wrist Arthritis • Hand, Wrist &amp; Elbow Tendonitis<br>
    Fractures of the Hand, Wrist, Elbow and Humerus<br>
    Nerve Injuries of the Hand, Wrist &amp; Elbow<br>
    Microsurgery • Wrist Arthroscopy • Endoscopic Surgery
  </p>
</section>

<section class="card card-front">
  <span class="edge-tab"></span>
  <div class="headshot" role="img" aria-label="Headshot portrait of the surgeon in a dark blazer"></div>
  <div class="hand-art" role="img" aria-label="Light blue line illustration of an open hand"></div>

  <div class="details">
    <h1 class="doctor-name">DANA WELLS, M.D.</h1>
    <p class="credentials">Board Certified<br>Orthopaedic Hand &amp; Upper<br>Extremity Surgeon</p>
    <p class="address">4382 NW 58th Lane, Suite 305<br>Tamarac, FL 33417</p>
    <ul class="contact-list">
      <li>
        <svg viewBox="0 0 16 16" aria-hidden="true"><rect x="4" y="1" width="8" height="14" rx="1.5" fill="none" stroke="var(--teal)" stroke-width="1.6"/><circle cx="8" cy="12.3" r="0.9" fill="var(--teal)"/></svg>
        (585) 314-9062
      </li>
      <li>
        <svg viewBox="0 0 16 16" aria-hidden="true"><path d="M3 2.5l2.5-.5 1.3 3-1.5 1.2a8 8 0 0 0 4.5 4.5l1.2-1.5 3 1.3-.5 2.5C8 13.5 2.5 8 3 2.5z" fill="var(--teal)"/></svg>
        (954) 316-4870
      </li>
      <li>
        <svg viewBox="0 0 16 16" aria-hidden="true"><rect x="4" y="1.5" width="8" height="4" fill="none" stroke="var(--teal)" stroke-width="1.4"/><rect x="1.5" y="6" width="13" height="6" rx="1" fill="var(--teal)"/><rect x="4" y="10" width="8" height="4.5" fill="var(--white)" stroke="var(--teal)" stroke-width="1.4"/></svg>
        (954) 316-4881
      </li>
      <li>
        <svg viewBox="0 0 16 16" aria-hidden="true"><rect x="1.5" y="3.5" width="13" height="9" rx="1" fill="var(--teal)"/><path d="M2 4.5l6 4.5 6-4.5" fill="none" stroke="var(--white)" stroke-width="1.2"/></svg>
        info@wellsorthocare.example
      </li>
      <li>
        <svg viewBox="0 0 16 16" aria-hidden="true"><circle cx="8" cy="8" r="6.5" fill="var(--teal)"/><path d="M1.5 8h13M8 1.5c-3 3.5-3 9.5 0 13M8 1.5c3 3.5 3 9.5 0 13" fill="none" stroke="var(--white)" stroke-width="1"/></svg>
        www.wellsorthocare.example
      </li>
    </ul>
  </div>
</section>

</body>
</html>
```